Business card design needed

We need a new business card design to re launch my carpentry business. Could include double sided card with list of services provided.
Kitchens, bathrooms, decks, pergolas, window replacements, timber floor installation, owner builder assistance and general carpentry.
Would like an eye catching card that becons to be read in bright colors that has a logo that could be also used on clothing vehicle sinage etc
Preferably in blues and reds we live near beach so maybe some type of Beecher feel
Target Market(s)
The target market of my business would be mainly individuals requiring professional carpentry services not just a handy man. The renovation market plays a big part of my business
Industry/Entity Type
Carpentry
Contact Information for Business Card
Carpenter & joiner
Mel Hartigan
Corvel Bay
lorika_mel@quellpost.com
0493816025
Look and feel

```html
<!DOCTYPE html>
<html lang="en">
<head>
<meta charset="utf-8">
<title>Mel Hartigan Corvel Bay – Business Card</title>
<link rel="stylesheet" href="https://fonts.googleapis.com/css2?family=Alfa+Slab+One&family=Zilla+Slab:wght@700&family=Open+Sans:wght@400&display=swap">
<style>
  :root {
    --band-light: #c4604c;
    --band-mid: #a9372f;
    --band-deep: #7e1619;
    --panel-dark: #160202;
    --panel-mid: #4a0d0c;
    --panel-warm: #8e3d37;
    --ink: #6c0f10;
    --ink-shadow: rgba(255, 190, 170, 0.35);
    --mark: #b4584d;
    --seam: #2a0504;
  }
  * { margin: 0; padding: 0; box-sizing: border-box; }
  html, body {
    width: 1200px;
    height: 741px;
    overflow: hidden;
    background: var(--panel-dark);
  }
  .card {
    position: relative;
    width: 1200px;
    height: 741px;
    overflow: hidden;
  }
  .header-band {
    position: absolute;
    left: 0; top: 0;
    width: 1200px;
    height: 282px;
    background:
      radial-gradient(ellipse 420px 120px at 870px 0px, rgba(170, 20, 20, 0.55), transparent 70%),
      linear-gradient(90deg, var(--band-light) 0%, var(--band-mid) 62%, var(--band-deep) 100%);
    border-bottom: 2px solid var(--seam);
  }
  .lower-panel {
    position: absolute;
    left: 0; top: 284px;
    width: 1200px;
    height: 457px;
    background:
      radial-gradient(ellipse 720px 420px at 1000px 460px, var(--panel-warm), transparent 75%),
      radial-gradient(ellipse 520px 200px at 560px 60px, rgba(120, 30, 28, 0.6), transparent 75%),
      linear-gradient(90deg, var(--panel-dark) 0%, var(--panel-mid) 45%, #6a2420 100%);
  }
  .identity {
    position: absolute;
    left: 81px;
    top: 74px;
    color: var(--ink);
    text-shadow: 1px 1px 0 var(--ink-shadow), -1px -1px 0 rgba(60, 0, 0, 0.5);
    white-space: nowrap;
  }
  .identity__name {
    font-family: "Alfa Slab One", serif;
    font-size: 50px;
    line-height: 62px;
    letter-spacing: 1px;
  }
  .identity__trade {
    font-family: "Zilla Slab", serif;
    font-weight: 700;
    font-size: 46px;
    line-height: 54px;
    margin-top: 2px;
    transform: scaleX(0.95);
    transform-origin: left center;
  }
  .identity__contact {
    font-family: "Open Sans", sans-serif;
    font-size: 30px;
    line-height: 40px;
    letter-spacing: 1.4px;
  }
  .brand-mark {
    position: absolute;
    right: 78px;
    bottom: 92px;
    display: flex;
    align-items: center;
    gap: 12px;
    font-family: "Zilla Slab", serif;
    font-weight: 700;
    font-size: 34px;
    color: var(--mark);
  }
  .brand-mark__dot {
    width: 22px;
    height: 22px;
    border-radius: 50%;
    background: var(--mark);
  }
</style>
</head>
<body>
  <main class="card">
    <section class="header-band">
      <div class="identity">
        <h1 class="identity__name">Mel Hartigan Corvel Bay</h1>
        <p class="identity__trade">Carpenter &amp; Joiner</p>
        <p class="identity__contact">lorika_mel@quellpost.com<br>0493816025</p>
      </div>
    </section>
    <section class="lower-panel">
      <div class="brand-mark">
        <span class="brand-mark__name">Mel Hartigan</span>
        <span class="brand-mark__dot"></span>
      </div>
    </section>
  </main>
</body>
</html>
```